Corvale Homes

To produce a business card design for our newly established house building and development company, We have had a logo design done please see attached, our slogan is "Homes built around your life"
Contact Information for Business Card
Adress on card needs to Read - 58 Elmsworth Lane, Marlowby, Fenwickshire MB7 4QT. Director name Dean Vascotti
Requirements
Must have
- Web adress is www.corvale-homes.co.uk
- Email address is info@corvale-homes.co.uk
- phone number 07700 900417

```html
<!DOCTYPE html>
<html lang="en">
<head>
<meta charset="utf-8">
<title>Corvale Homes – Business Card</title>
<link rel="stylesheet" href="https://fonts.googleapis.com/css2?family=Lato:wght@400;700&display=swap">
<style>
  :root {
    --backdrop: #e6e6e4;
    --card: #ffffff;
    --header-grey: #646464;
    --header-grey-soft: #8a8a8a;
    --brand-green: #7cc242;
    --text-dark: #3a3a3a;
    --text-mid: #505050;
  }
  * { box-sizing: border-box; margin: 0; padding: 0; }
  html, body {
    width: 1200px; height: 900px; overflow: hidden;
    background: var(--backdrop);
    font-family: "Lato", Arial, sans-serif;
  }
  .business-card {
    position: absolute; left: 100px; top: 140px;
    width: 1000px; height: 620px;
    background: var(--card);
    overflow: hidden;
    box-shadow: 0 6px 24px rgba(0,0,0,0.12);
  }
  .header-art {
    position: absolute; left: 0; top: 0; width: 100%; height: 170px;
    background: linear-gradient(180deg, var(--header-grey) 0%, var(--header-grey) 70%, var(--header-grey-soft) 100%);
  }
  .brand {
    position: absolute; left: 0; width: 804px; top: 238px;
    text-align: center;
  }
  .brand-name {
    font-weight: 700; font-size: 60px; letter-spacing: 3px;
    color: var(--brand-green); line-height: 1;
  }
  .brand-slogan {
    margin-top: 16px;
    font-weight: 700; font-size: 13px; letter-spacing: 7px;
    color: var(--brand-green);
  }
  .contact-person {
    position: absolute; right: 64px; top: 386px; text-align: right;
  }
  .person-name {
    font-weight: 700; font-size: 33px; color: var(--brand-green); line-height: 1.1;
  }
  .person-role { font-size: 26px; color: var(--text-mid); margin-top: 4px; }
  .contact-list {
    position: absolute; left: 56px; top: 447px; list-style: none;
  }
  .contact-list li {
    display: flex; align-items: center; gap: 10px;
    font-size: 27px; color: var(--text-dark); height: 34px;
  }
  .contact-list svg { width: 20px; height: 20px; fill: var(--brand-green); flex: none; }
  .address {
    position: absolute; right: 64px; top: 481px; text-align: right;
    font-size: 27px; color: var(--text-dark); line-height: 34px; font-style: normal;
  }
  .base-band {
    position: absolute; left: 0; bottom: 0; width: 100%; height: 20px;
    background: var(--brand-green);
  }
</style>
</head>
<body>
  <div class="business-card">
    <div class="header-art" role="img" aria-label="Decorative house roofline with chimney across the top of the card"></div>

    <div class="brand">
      <div class="brand-name">CORVALE HOMES</div>
      <div class="brand-slogan">HOMES BUILT AROUND YOUR LIFE</div>
    </div>

    <div class="contact-person">
      <div class="person-name">DEAN VASCOTTI</div>
      <div class="person-role">Director</div>
    </div>

    <ul class="contact-list">
      <li>
        <svg viewBox="0 0 24 24"><path d="M6.6 10.8a15.1 15.1 0 0 0 6.6 6.6l2.2-2.2a1 1 0 0 1 1-.25 11.4 11.4 0 0 0 3.6.57 1 1 0 0 1 1 1V20a1 1 0 0 1-1 1A17 17 0 0 1 3 4a1 1 0 0 1 1-1h3.5a1 1 0 0 1 1 1c0 1.25.2 2.45.57 3.57a1 1 0 0 1-.25 1z"/></svg>
        07700 900417
      </li>
      <li>
        <svg viewBox="0 0 24 24"><path d="M2 5h20v14H2z"/><path d="M3 6.5l9 6.5 9-6.5" fill="none" stroke="#fff" stroke-width="1.6"/></svg>
        info@corvale-homes.co.uk
      </li>
      <li>
        <svg viewBox="0 0 24 24"><circle cx="12" cy="12" r="10"/><path d="M2 12h20M12 2c3 3 3 17 0 20M12 2c-3 3-3 17 0 20" fill="none" stroke="#fff" stroke-width="1.4"/></svg>
        www.corvale-homes.co.uk
      </li>
    </ul>

    <address class="address">
      58 Elmsworth Lane, Marlowby<br>
      Fenwickshire MB7 4QT
    </address>

    <div class="base-band"></div>
  </div>
</body>
</html>
```